Flyer für Beratung rund um den Computer
Zielgruppe
Hauptsächlich: Beratung rund um den Computer, individuelle Schulungen, technische Hilfe . Aber auch: Einführung in die Programmierung, Webseitenerstellung etc. Zielgruppe sind Privatpersonen, gerne auch ältere Personen, alle die sich unsicher im Umgang mit Computern fühlen und freundliche, geduldige Hilfe suchen.
Aufgabenstellung
Da meine Zielgruppe eher keine Computerfreaks sind, sollte der Flyer nicht zu technisch aussehen, sondern für Hilfesuchende ansprechend und freundlich wirken.

```html
<!DOCTYPE html>
<html lang="de">
<head>
<meta charset="utf-8">
<title>Flyer – PC ganz leicht</title>
<link href="https://fonts.googleapis.com/css2?family=Amatic+SC:wght@400;700&family=Rubik:wght@400;500;700&family=Mrs+Saint+Delafield&display=swap" rel="stylesheet">
<style>
:root{
  --bg:#e6e6e8;
  --paper:#ffffff;
  --brown:#3a1a12;
  --sky:#b5dfea;
  --sky-text:#8ccbe0;
  --ink:#4a3a35;
  --ink-soft:#6b5d58;
  --photo-a:#f4ead6;
  --photo-b:#c9b99a;
  --photo-c:#8a7a62;
}
*{margin:0;padding:0;box-sizing:border-box}
html,body{width:1200px;height:960px;overflow:hidden;background:var(--bg)}
body{font-family:"Rubik",sans-serif;color:var(--ink);position:relative}
.flyer{position:absolute;top:84px;width:560px;height:792px;background:var(--paper);overflow:hidden;box-shadow:0 10px 30px rgba(0,0,0,.12)}
.flyer--front{left:27px}
.flyer--back{left:613px}

/* front */
.photo{position:absolute;left:0;top:0;width:560px;height:430px;
  background:radial-gradient(ellipse at 65% 45%,var(--photo-b) 0%,var(--photo-a) 45%,rgba(255,255,255,0) 75%),
  linear-gradient(160deg,rgba(255,255,255,.9) 0%,rgba(244,234,214,.4) 40%,var(--photo-c) 100%);}
.photo::after{content:"";position:absolute;inset:0;background:linear-gradient(to bottom,rgba(255,255,255,0) 60%,#fff 100%),linear-gradient(to right,#fff 0%,rgba(255,255,255,0) 35%)}
.brand{position:absolute;left:36px;top:34px;display:flex;align-items:center;gap:10px;z-index:2}
.brand__dot{width:18px;height:18px;border-radius:50%;background:var(--sky)}
.brand__name{font-family:"Rubik",sans-serif;font-weight:500;font-size:17px;letter-spacing:2px;color:var(--sky-text);text-transform:uppercase}
.intro{position:absolute;left:36px;top:455px;width:325px;display:flex;flex-direction:column;gap:10px;z-index:1}
.intro__title{font-family:"Amatic SC",sans-serif;font-size:30px;font-weight:400;color:var(--sky-text);line-height:1}
.intro__text{font-size:11px;line-height:1.55;color:var(--ink-soft)}
.intro__call{font-size:11px;font-weight:700;line-height:1.55;color:var(--ink)}
.badge{position:absolute;border-radius:50%;background:var(--sky);display:flex;flex-direction:column;align-items:center;justify-content:center;color:#fff;text-align:center}
.badge--phone{left:372px;top:400px;width:170px;height:170px;z-index:2}
.badge--phone .num{font-size:19px;font-weight:500;letter-spacing:1px;margin-top:6px}
.badge--phone .lbl{font-size:12.5px;font-weight:500;color:var(--ink);line-height:1.2;margin-top:4px}
.quote{position:absolute;left:36px;top:712px;width:490px;font-family:"Mrs Saint Delafield",cursive;font-size:28px;line-height:1.05;color:var(--ink)}
.quote__mark{position:absolute;left:10px;top:684px;font-family:"Rubik",sans-serif;font-weight:700;font-size:34px;color:var(--sky)}
.dots circle{fill:var(--sky);opacity:.6}

/* back */
.services__title{position:absolute;left:36px;top:40px;font-family:"Amatic SC",sans-serif;font-size:36px;color:var(--sky-text)}
.service{position:absolute;width:150px;text-align:center}
.service__icon{width:96px;height:96px;margin:0 auto 12px;border-radius:50%;background:var(--sky);display:flex;align-items:center;justify-content:center}
.service__name{font-size:15px;font-weight:700;color:var(--ink);line-height:1.2}
.service__desc{font-size:11px;line-height:1.5;color:var(--ink-soft);margin-top:6px}
.panel{position:absolute;right:0;top:0;width:230px;height:792px}
.contact{position:absolute;left:382px;top:470px;width:160px;color:#fff}
.contact__title{font-family:"Amatic SC",sans-serif;font-size:32px;font-weight:700;letter-spacing:1px;margin-bottom:10px}
.contact__day{font-size:11.5px;font-weight:500;color:var(--sky)}
.contact__time{font-size:11.5px;margin-bottom:10px;opacity:.9}
.contact__row{display:flex;gap:10px;align-items:flex-start;font-size:11.5px;line-height:1.4;margin-top:14px}
.contact__row svg{flex:none;margin-top:1px}
</style>
</head>
<body>

<section class="flyer flyer--front">
  <div class="photo" role="img" aria-label="Foto eines hellen Schreibtischs mit Laptop, Brille, Kaffeetasse und Pflanze"></div>
  <div class="brand"><span class="brand__dot"></span><span class="brand__name">PC ganz leicht</span></div>
  <div class="badge badge--phone">
    <svg width="32" height="42" viewBox="0 0 34 44"><rect x="2" y="2" width="30" height="40" rx="5" fill="none" stroke="#fff" stroke-width="2.5"/><line x1="13" y1="36" x2="21" y2="36" stroke="#fff" stroke-width="2.5"/></svg>
    <div class="num">0160 555 0182</div>
    <div class="lbl">Telefonische<br>Beratung</div>
  </div>
  <div class="intro">
    <h1 class="intro__title">Computer – alles, nur kein Hexenwissen</h1>
    <p class="intro__text">Ganz egal, was Sie im Zusammenhang mit Ihrem Rechner umtreibt – ob Sie sich manchmal einfach etwas unsicher fühlen, mit einer Anwendung nicht zurecht kommen oder Ihr Rechner nicht so reagiert, wie er sollte – mein Ziel ist es, dass Sie sich im Umgang mit Ihrem Computer sicher fühlen und Freude daran haben.</p>
    <p class="intro__call">Also: Legen Sie los – egal wie klein oder groß Ihre Frage ist – ich helfe gerne!</p>
  </div>
  <span class="quote__mark">”</span>
  <p class="quote">Denken ist ein Lauschen im Schweigen, Beratung der Gedanken von Herz und Verstand.</p>
  <svg class="dots" width="560" height="792" style="position:absolute;left:0;top:0;pointer-events:none"><circle cx="410" cy="610" r="3"/><circle cx="520" cy="640" r="4"/><circle cx="30" cy="770" r="3"/><circle cx="470" cy="690" r="3"/><circle cx="400" cy="660" r="2"/></svg>
</section>

<section class="flyer flyer--back">
  <h2 class="services__title">Meine Leistungen im Überblick</h2>

  <div class="service" style="left:30px;top:110px">
    <div class="service__icon"><svg width="54" height="44" viewBox="0 0 54 44" fill="none" stroke="#fff" stroke-width="2"><path d="M4 4h30v20H16l-8 7v-7H4z"/><path d="M38 14h12v18h-4v6l-7-6H22v-4"/></svg></div>
    <div class="service__name">Beratung rund um Ihren Rechner</div>
    <div class="service__desc">Kauf, Organisation, Anwendungen, Optimierung, Internet, Datensicherung, …</div>
  </div>
  <div class="service" style="left:200px;top:200px">
    <div class="service__icon"><svg width="50" height="46" viewBox="0 0 50 46" fill="none" stroke="#fff" stroke-width="2"><rect x="4" y="6" width="42" height="26"/><line x1="2" y1="6" x2="48" y2="6"/><line x1="25" y1="32" x2="25" y2="42"/><line x1="18" y1="44" x2="32" y2="44"/></svg></div>
    <div class="service__name">Individuelle Schulungen</div>
    <div class="service__desc">allgemeiner Umgang mit dem Rechner, Nutzung bestimmter Anwendungen, …</div>
  </div>
  <div class="service" style="left:30px;top:390px">
    <div class="service__icon"><svg width="48" height="48" viewBox="0 0 48 48" fill="none" stroke="#fff" stroke-width="2"><path d="M8 40L30 18a8 8 0 1 1 6 6L14 46z"/><path d="M10 8l8 8-4 4-8-8z"/><path d="M18 16l22 22-4 4-22-22"/></svg></div>
    <div class="service__name">Technische Hilfe</div>
    <div class="service__desc">Anschluss bzw. Einbinden von Peripheriegeräten, kleine Reparaturen, …</div>
  </div>
  <div class="service" style="left:200px;top:480px">
    <div class="service__icon"><svg width="46" height="46" viewBox="0 0 46 46" fill="none" stroke="#fff" stroke-width="2"><rect x="4" y="4" width="16" height="16"/><rect x="26" y="4" width="16" height="16"/><rect x="4" y="26" width="16" height="16"/><rect x="26" y="26" width="16" height="16"/></svg></div>
    <div class="service__name">Für alle, die mehr wollen</div>
    <div class="service__desc">Einführung in die Programmierung, Erstellen von Websites, KI, …</div>
  </div>

  <svg class="panel" viewBox="0 0 230 792" preserveAspectRatio="none" aria-hidden="true">
    <path d="M230 0V792H20c8-30-6-55 6-85s-10-50 2-80-8-60 4-90 14-45 0-75 14-60 4-90 12-40 18-65-4-40 6-70 20-45 10-75 12-30 30-55 10-50 22-60 30-8 40-12z" fill="var(--brown)"/>
  </svg>

  <div class="contact">
    <h3 class="contact__title">Erreichbarkeit</h3>
    <div class="contact__day">Montag bis Freitag</div>
    <div class="contact__time">09:00 – 19:00 Uhr</div>
    <div class="contact__day">Samstag</div>
    <div class="contact__time">09:00 – 14:00 Uhr</div>
    <div class="contact__row"><svg width="14" height="18" viewBox="0 0 14 18" fill="none" stroke="#fff" stroke-width="1.5"><rect x="1" y="1" width="12" height="16" rx="2"/><line x1="5" y1="14" x2="9" y2="14"/></svg><span>0160 555 0182</span></div>
    <div class="contact__row"><svg width="16" height="12" viewBox="0 0 16 12" fill="none" stroke="#fff" stroke-width="1.5"><rect x="1" y="1" width="14" height="10"/><path d="M1 1l7 6 7-6"/></svg><span>lena@pc-ganz-leicht.de</span></div>
    <div class="contact__row"><svg width="16" height="16" viewBox="0 0 16 16" fill="none" stroke="#fff" stroke-width="1.3"><circle cx="8" cy="8" r="7"/><ellipse cx="8" cy="8" rx="3" ry="7"/><line x1="1" y1="8" x2="15" y2="8"/></svg><span>www.pc-ganz-leicht.de</span></div>
  </div>

  <svg class="dots" width="560" height="792" style="position:absolute;left:0;top:0;pointer-events:none"><circle cx="180" cy="120" r="3"/><circle cx="300" cy="150" r="4"/><circle cx="170" cy="350" r="3"/><circle cx="330" cy="430" r="2"/><circle cx="20" cy="700" r="3"/><circle cx="150" cy="740" r="4"/></svg>
</section>

</body>
</html>
```